Property Finance Company - Orca Ridge Limited

Background: Orca Ridge Group Limited is a private property finance company. Orca Ridge Group has capital to directly fund first mortgage, mezzanine and preferred equity financing. We also acquire performing, sub-performing and distressed debt.

Orca Ridges management philosophy emphasises expertise, innovation, wisdom, honesty and competitiveness. Orca Ridge are not finance brokers - we provide debt funding to the commercial property and residential development sectors. Our process is built from experience and cumutavely Orca Ridges Directors have in excess of 60 years wisdom.

The aim of the website will be to increase brand awareness, provide clients with comfort around our level of skill and background on who we are, generate more sales, and provide examples of projects that we have funded.

The website is a new product launch, and we need to use our Orca Ridge logo that has just been designed. We like a dark background, and either black/silver/grey/ jade green, or black/gold/jade green colours.

Our unique advantages are that we have fast turnaround times, we can solve clients funding problems and we know what we are doing. Our target audience will be viewing the website on both desktop and mobile devices.

We would like to have the following pages:

Home
About
Team
Services
Project Experience
Contact

Competitors Website: http://www.vbtq.example/

We would also like to have the option of video footage in our website, as you can see in our competitors website.

Overall we want a really slick, elegant but modern website that is better than www.vbtq.example

Target Market(s)

Finance borrowers, property developers, accountants, lawyers, businesspeople, high net worth people

Industry/Entity Type

Finance

Requirements
Must have
• Please see project description
Nice to have
Should not have

```html
<!DOCTYPE html>
<html lang="en">
<head>
<meta charset="utf-8">
<title>Orca Ridge Group — Property Finance</title>
<link href="https://fonts.googleapis.com/css2?family=Libre+Franklin:wght@400;500;600;700&display=swap" rel="stylesheet">
<style>
:root{
  --jade:#0fa36b;
  --ink:#1c1c1c;
  --text:#3a3a3a;
  --muted:#8a8a8a;
  --rule:#dcdfe4;
  --pale:#f3f5f9;
  --dark:#231f20;
  --white:#ffffff;
}
*{box-sizing:border-box;margin:0;padding:0}
html,body{width:1200px;height:3175px;overflow:hidden}
body{font-family:"Libre Franklin",Arial,sans-serif;color:var(--text);background:var(--white);position:relative}
.abs{position:absolute}
a{color:inherit;text-decoration:none}
.green{color:var(--jade)}
.u{text-decoration:underline}

/* hero */
.hero{top:0;left:0;width:1200px;height:643px}
.hero-photo{left:0;top:0;width:916px;height:643px;background:linear-gradient(120deg,#4b5055 0%,#7c8388 45%,#5d6368 75%,#3f4347 100%)}
.brand{left:76px;top:86px;color:var(--white);font-size:20px;font-weight:600;letter-spacing:.5px;display:flex;align-items:center;gap:10px}
.brand .dot{width:22px;height:22px;border-radius:50%;border:2px solid var(--white)}
.hero-copy{left:127px;top:244px;color:var(--white)}
.hero-copy .kicker{font-size:13px;font-weight:600}
.hero-copy h1{font-size:31px;font-weight:600;line-height:36px;margin-top:6px}
.hero-copy .sub{font-size:13px;font-weight:600;line-height:18px;margin-top:12px}
.hero-copy .more{font-size:12px;font-weight:600;margin-top:34px;display:block}
.watch{left:127px;top:552px;color:var(--white);font-size:13px;font-weight:600;display:flex;align-items:center;gap:12px}
.mouse{left:590px;top:540px}
.menu{left:916px;top:0;width:284px;height:643px;background:rgba(243,244,246,.94)}
.menu .close{position:absolute;left:22px;top:48px}
.menu nav{position:absolute;left:26px;top:122px;font-size:17px;font-weight:600;color:var(--ink);line-height:29px}
.menu nav a{display:block}
.menu nav a.on{color:var(--jade)}
.menu .contact{position:absolute;left:26px;top:404px;color:var(--ink)}
.menu .contact .lbl{font-size:13px;font-weight:600}
.menu .contact .tel{font-size:19px;margin-top:22px}
.menu .contact .mail{font-size:12px;font-weight:600}
.socials{display:flex;gap:7px}
.socials span{width:32px;height:32px;border-radius:50%;background:var(--ink);display:block}
.socials span.on{background:var(--jade)}
.menu .socials{position:absolute;left:26px;top:549px}

/* section frame */
.sec-head{left:127px;font-size:30px;font-weight:500;color:var(--ink)}
.hline{height:1px;background:var(--rule);left:76px;width:1048px}
.vline{width:1px;background:var(--rule);left:381px}
.link-r{font-size:12px;font-weight:600;color:var(--ink);right:155px}

/* about */
.about{top:643px;left:0;width:1200px;height:485px}
.about .lead{left:127px;top:189px;width:230px;font-size:15px;font-weight:600;color:var(--ink);line-height:20px}
.about .body{left:434px;top:60px;width:405px}
.about .body p{font-size:14px;line-height:20px;color:var(--ink);margin-bottom:20px}
.about .body p.small{font-size:12.5px;color:var(--muted);line-height:20px}
.btn{display:inline-block;background:var(--jade);color:var(--white);font-size:12px;font-weight:600;padding:10px 22px}
.about .btn{left:434px;top:387px}
.shot{background:linear-gradient(135deg,#8b9298,#c9cdd1 50%,#6f777d)}

/* services */
.services{top:1128px;left:0;width:1200px;height:482px;background:var(--pale)}
.svc{top:148px;width:290px}
.svc h3{font-size:15px;font-weight:600;color:var(--ink)}
.svc p{font-size:12.5px;line-height:19.5px;color:var(--muted);margin-top:18px}
.svc .rm{position:absolute;top:242px;font-size:12px;font-weight:600;color:var(--ink)}

/* projects */
.projects{top:1610px;left:0;width:1200px;height:644px}
.card{color:var(--white);overflow:hidden}
.card .t{position:absolute;left:24px;bottom:30px;font-size:15px;font-weight:600}
.card .s{position:absolute;left:24px;bottom:14px;font-size:11px;font-weight:500}
.card.feature{background:rgba(15,163,107,.92);padding:22px 24px}
.card.feature h4{font-size:16px;font-weight:600}
.card.feature .c{font-size:12px;font-weight:600;margin-top:4px}
.card.feature .d{font-size:13px;line-height:19px;margin-top:20px}
.card.feature .rm{font-size:12px;font-weight:600;margin-top:18px;display:block}

/* team */
.team{top:2254px;left:0;width:1200px;height:565px;background:var(--pale)}
.dots{left:990px;top:85px;display:flex;gap:9px}
.dots span{width:8px;height:8px;border-radius:50%;background:#c5c9cf}
.dots span.on{background:var(--jade)}
.member{top:156px;width:275px;background:var(--white)}
.member .ph{height:214px;background:linear-gradient(160deg,#b9a79a,#8c7a6f)}
.member .nm{height:63px;text-align:center;padding-top:15px}
.member .nm b{display:block;font-size:15px;font-weight:600;color:var(--ink)}
.member .nm i{display:block;font-style:normal;font-size:11px;color:var(--muted);margin-top:3px}
.member.on .nm{background:var(--jade)}
.member.on .nm b,.member.on .nm i{color:var(--white)}
.btn-o{left:535px;top:467px;width:132px;height:32px;border:1px solid var(--jade);font-size:12px;font-weight:600;color:var(--ink);text-align:center;line-height:30px;background:var(--white)}

/* footer */
.footer{top:2819px;left:0;width:1200px;height:356px;background:var(--dark);color:var(--white)}
.footer .sec-head{color:var(--white)}
.footer .hline,.footer .vline{background:#4a4546}
.footer .brand{left:127px;top:170px}
.fcol{top:165px}
.fcol h5{font-size:14px;font-weight:600}
.fcol p{font-size:12.5px;line-height:20px;color:#a9a5a6;margin-top:22px}
.fcol .tel{font-size:19px;color:#d0cdcd;margin-top:20px}
.fcol .mail{font-size:12px;color:#d0cdcd}
.footer .socials span{background:#8d8889}
.footer .socials span.on{background:var(--jade)}
.copy{left:127px;top:311px;font-size:12px;color:#c9c5c6}
.top-btn{left:1022px;top:307px;width:22px;height:22px;border-radius:50%;background:var(--jade)}
</style>
</head>
<body>

<header class="hero abs">
  <div class="hero-photo abs" role="img" aria-label="Two businessmen meeting at a table with a laptop in a glass office"></div>
  <div class="brand abs"><span class="dot"></span>Orca Ridge Group</div>
  <div class="hero-copy abs">
    <div class="kicker">Orca Ridge Group</div>
    <h1>We Provide Debt<br>Funding</h1>
    <div class="sub">to the commercial property and<br>residential development sectors</div>
    <a class="more" href="#">Explore More →</a>
  </div>
  <div class="watch abs">
    <svg width="28" height="28" viewBox="0 0 28 28"><circle cx="14" cy="14" r="12.5" fill="none" stroke="#fff" stroke-width="2"/><path d="M11 8.5 L19.5 14 L11 19.5Z" fill="#fff"/></svg>
    Watch Video
  </div>
  <svg class="mouse abs" width="18" height="34" viewBox="0 0 18 34"><rect x="1" y="1" width="16" height="32" rx="8" fill="none" stroke="#fff" stroke-width="2"/><rect x="8" y="8" width="2" height="7" rx="1" fill="#fff"/></svg>

  <aside class="menu abs">
    <svg class="close" width="26" height="26" viewBox="0 0 26 26"><path d="M2 2L24 24M24 2L2 24" stroke="#0fa36b" stroke-width="2.5"/></svg>
    <nav>
      <a class="on" href="#">Home</a>
      <a href="#">About</a>
      <a href="#">Team</a>
      <a href="#">Services</a>
      <a href="#">Project Experience</a>
      <a href="#">Contact Us</a>
    </nav>
    <div class="contact">
      <div class="lbl">Contact Us</div>
      <div class="tel">555 - 201 - 4830</div>
      <div class="mail"><span class="green u">E-mail</span> Us.</div>
    </div>
    <div class="socials"><span></span><span class="on"></span><span></span><span></span></div>
  </aside>
</header>

<section class="about abs">
  <h2 class="sec-head abs" style="top:60px;line-height:36px">About<br>Company</h2>
  <div class="hline abs" style="top:155px;width:305px"></div>
  <div class="vline abs" style="top:0;height:485px"></div>
  <p class="lead abs">Orca Ridge Group Limited is a Private Property Finance Company.</p>
  <div class="body abs">
    <p>Orca Ridge Group has capital to directly fund first mortgage, mezzanine and preferred equity financing. We also acquire performing, sub-performing and distressed debt.</p>
    <p class="small">Orca Ridges management philosophy emphasises expertise, innovation, wisdom, honesty and competitiveness. Orca Ridge are not finance brokers - we provide debt funding to the commercial property and residential development sectors.</p>
    <p>Our process is built from experience and cumutavely <span class="green">Orca Ridges Directors have in excess of 60 years wisdom.</span></p>
  </div>
  <a class="btn abs" href="#">Discover More</a>
  <div class="shot abs" style="left:916px;top:0;width:284px;height:241px" role="img" aria-label="Business partners reviewing documents at an office table"></div>
  <div class="shot abs" style="left:916px;top:244px;width:284px;height:241px" role="img" aria-label="Team of colleagues working together on laptops"></div>
</section>

<section class="services abs">
  <h2 class="sec-head abs" style="top:62px">Our Services</h2>
  <div class="vline abs" style="top:0;height:118px"></div>
  <div class="hline abs" style="top:118px"></div>
  <a class="link-r abs" href="#" style="top:70px">View All Services →</a>
  <div class="svc abs" style="left:127px">
    <h3>Development Finance</h3>
    <p>There are many variations of passages of Lorem Ipsum available, but the majority have suffered alteration in some form, by injected humour, or randomised words which don't look even slightly believable.<br>If you are going to use a passage of Lorem Ipsum...</p>
    <a class="rm" href="#">Read More →</a>
  </div>
  <div class="svc abs" style="left:434px">
    <h3>Bridging Finance</h3>
    <p>There are many variations of passages of Lorem Ipsum available, but the majority have suffered alteration in some form, by injected humour, or randomised words which don't look even slightly believable.<br>If you are going to use a passage of Lorem Ipsum...</p>
    <a class="rm green u" href="#">Read More →</a>
  </div>
  <div class="svc abs" style="left:739px">
    <h3>Bank Finance</h3>
    <p>There are many variations of passages of Lorem Ipsum available, but the majority have suffered alteration in some form, by injected humour, or randomised words which don't look even slightly believable.<br>If you are going to use a passage of Lorem Ipsum...</p>
    <a class="rm" href="#">Read More →</a>
  </div>
</section>

<section class="projects abs">
  <h2 class="sec-head abs" style="top:62px">Our Projects</h2>
  <div class="vline abs" style="top:0;height:121px"></div>
  <div class="hline abs" style="top:121px"></div>
  <a class="link-r abs green u" href="#" style="top:76px">View All Projects →</a>

  <div class="card abs" style="left:127px;top:155px;width:283px;height:201px;background:linear-gradient(160deg,#c8d2da,#8a969c 60%,#5a6a4e)" role="img" aria-label="Modern white residential building with balconies">
    <div class="t">Queen Residences</div><div class="s">Centuries</div>
  </div>
  <div class="card feature abs" style="left:434px;top:155px;width:611px;height:201px">
    <h4>Commercial Offices</h4>
    <div class="c">Centuries</div>
    <div class="d">$14,000,000 low prise office building.<br>15 units.<br>Completed October 2016</div>
    <a class="rm" href="#">Read More →</a>
  </div>
  <div class="card abs" style="left:127px;top:379px;width:588px;height:201px;background:linear-gradient(90deg,#4f5a66,#7b8894 55%,#3f7fb5 80%,#6aa6d6)" role="img" aria-label="Apartment building facade against blue sky">
    <div class="t">Aria Apartments</div><div class="s">Centuries</div>
  </div>
  <div class="card abs" style="left:741px;top:379px;width:304px;height:201px;background:linear-gradient(150deg,#9fb4c8,#5f7488 60%,#3c4c5c)" role="img" aria-label="Glass commercial tower viewed from below">
    <div class="t">Commercial Building</div><div class="s">Centuries</div>
  </div>
</section>

<section class="team abs">
  <h2 class="sec-head abs" style="top:58px">Our Team</h2>
  <div class="vline abs" style="top:0;height:122px"></div>
  <div class="hline abs" style="top:122px"></div>
  <div class="dots abs"><span></span><span class="on"></span><span></span><span></span></div>
  <div class="member abs" style="left:127px">
    <div class="ph" role="img" aria-label="Portrait photo of team member"></div>
    <div class="nm"><b>Tavi Ormond</b><i>Director</i></div>
  </div>
  <div class="member on abs" style="left:451px">
    <div class="ph" style="background:linear-gradient(160deg,#e8e2dc,#c9ad8a)" role="img" aria-label="Portrait photo of team member"></div>
    <div class="nm"><b>J. Pellworth</b><i>Director</i></div>
  </div>
  <div class="member abs" style="left:772px">
    <div class="ph" style="background:linear-gradient(160deg,#dcdcdc,#6b5c52)" role="img" aria-label="Portrait photo of team member"></div>
    <div class="nm"><b>Corin Vale</b><i>Director</i></div>
  </div>
  <a class="btn-o abs" href="#">View All Team</a>
</section>

<footer class="footer abs">
  <h2 class="sec-head abs" style="top:58px">Contact Us</h2>
  <div class="vline abs" style="top:0;height:122px"></div>
  <div class="hline abs" style="top:122px"></div>
  <a class="link-r abs green u" href="#" style="top:76px">Get Direction →</a>
  <div class="brand abs"><span class="dot"></span>Orca Ridge Group</div>
  <div class="fcol abs" style="left:434px">
    <h5>Address:</h5>
    <p>4410 Harbour Terrace<br>Blvd Eastmere, QL 20418</p>
  </div>
  <div class="fcol abs" style="left:677px">
    <h5>Call Us:</h5>
    <div class="tel">555 - 201 - 4830</div>
    <div class="mail"><span class="green u">E-mail</span> Us.</div>
  </div>
  <div class="fcol abs" style="left:912px">
    <h5>Get Social:</h5>
    <div class="socials" style="margin-top:26px"><span></span><span class="on"></span><span></span><span></span></div>
  </div>
  <div class="hline abs" style="top:285px"></div>
  <div class="copy abs">© 2017 <span class="green u">Orca Ridge Group</span>. All Rights Reserved</div>
  <div class="top-btn abs"><svg width="22" height="22" viewBox="0 0 22 22"><path d="M7 12.5L11 8.5L15 12.5" fill="none" stroke="#231f20" stroke-width="2"/></svg></div>
</footer>

</body>
</html>
```